Website for Fashion/Jewelry online seller

We would like a website design that can be used in wordpress. It will be important to be able to link instagram, twitter, etc posts on the bottom of site. We are to be a online seller of chic jewelry, art, fashion, and other home design industries. Currently we emphasize jewelry but as the years move forward, other products will be introduced as collections in home furnishings and primarily women's fashion. It will be important to have a “shop now” section where people can order products online so ecommerce will need to be set up at some point. The website should have the following feel: clean, modern, contemporary and chic. A lot of whites should be used with simple text and simple but elegant fonts. Best is to go to mirevantello.com to get the best idea of what we are wanting for the look and feel of the site.

Target Market(s)

upper social class people that are into fashion, jewelry, etc

Industry/Entity Type

Fashion

Number of Pages Required

5+ page

Font styles to use
Other font styles liked:
• go to daskorvin.com to see the font desired

Requirements
Must have
• Name of Company is Tide Hollow 7
Nice to have
• see project description
Should not have
• see project description

```html
<!DOCTYPE html>
<html lang="en">
<head>
<meta charset="utf-8">
<title>Tide Hollow 7 — Jewellery, Art and Fashion</title>
<link href="https://fonts.googleapis.com/css2?family=Bodoni+Moda:ital,wght@0,400;0,500;1,400&family=Lato:wght@400&display=swap" rel="stylesheet">
<style>
:root{
  --white:#ffffff;
  --ink:#111111;
  --text:#555555;
  --muted:#8a8a8a;
  --faint:#d9d9d9;
  --line:#cfcfcf;
  --footer:#000000;
  --hero-a:#2a1a12;
  --hero-b:#5b3a26;
  --serif:'Bodoni Moda', 'Didot', serif;
  --sans:'Lato', Arial, sans-serif;
}
*{box-sizing:border-box;margin:0;padding:0}
html,body{width:1200px;height:4255px;overflow:hidden;background:var(--white)}
body{position:relative;font-family:var(--serif);color:var(--ink)}
.abs{position:absolute}

/* header */
.site-header{position:absolute;left:0;top:0;width:1200px;height:76px;background:var(--white)}
.brand{position:absolute;left:100px;top:20px;font-family:var(--serif);font-size:30px;font-weight:400;color:var(--ink);letter-spacing:.5px}
.main-nav{position:absolute;left:462px;top:33px;display:flex;gap:0}
.main-nav a{font-size:11px;letter-spacing:1px;color:var(--ink);text-decoration:none;text-transform:uppercase;width:95px;text-align:center}
.cart{position:absolute;left:1072px;top:22px}

/* hero */
.hero{position:absolute;left:0;top:76px;width:1200px;height:704px;background:linear-gradient(100deg,var(--hero-a) 0%,var(--hero-b) 40%,#3a2418 70%,var(--hero-a) 100%)}
.hero-title{position:absolute;left:0;width:1200px;text-align:center;color:var(--white)}
.hero-kicker{top:296px;font-size:38px;letter-spacing:3px}
.hero-main{top:340px;font-size:76px;font-style:italic;letter-spacing:2px;line-height:1.1}
.hero-sub{top:422px;font-size:38px;letter-spacing:3px}
.slider-dots{position:absolute;left:1148px;top:292px;display:flex;flex-direction:column;gap:16px}
.slider-dots span{width:9px;height:9px;border-radius:50%;background:rgba(255,255,255,.55)}
.slider-dots span.on{background:var(--white)}

/* welcome */
.welcome{position:absolute;left:100px;top:872px;width:470px}
.eyebrow{font-size:26px;letter-spacing:2px;text-transform:uppercase}
.display{font-size:62px;font-style:italic;letter-spacing:1px;line-height:1.1;text-transform:uppercase}
.copy{font-family:var(--sans);font-size:12px;line-height:22px;color:var(--text);margin-top:30px}
.btn{display:inline-block;border:1px solid #777;padding:8px 18px;font-size:10px;letter-spacing:1.5px;text-transform:uppercase;color:var(--ink);text-decoration:none}
.welcome .btn{position:absolute;top:347px;left:0}
.welcome-photo{position:absolute;left:655px;top:836px;width:446px;height:454px;background:radial-gradient(circle at 50% 45%,#6a4a34,#3b271b 70%,#2a1c14)}

/* offer heading */
.offer-bg{position:absolute;left:0;top:1355px;width:1200px;text-align:center;font-size:108px;color:var(--faint);letter-spacing:4px}
.offer-kicker{position:absolute;left:0;top:1408px;width:1200px;text-align:center;font-size:26px;letter-spacing:2px}
.offer-title{position:absolute;left:0;top:1440px;width:1200px;text-align:center;font-size:62px;font-style:italic;letter-spacing:1px}

/* collection tiles */
.tile{position:absolute}
.tile-photo{position:absolute;inset:0}
.card{position:absolute;background:var(--white);border:1px solid var(--line);outline:8px solid rgba(255,255,255,.6);text-align:center;padding:20px 14px 0}
.card-tag{font-size:9px;letter-spacing:2px;text-transform:uppercase}
.card-title{font-size:30px;text-transform:uppercase;line-height:1.1;margin-top:8px}
.card-title.italic{font-style:italic}
.card-sub{font-size:19px;font-style:italic;text-transform:uppercase}
.card-sub.small{font-size:16px;text-transform:lowercase}
.card-copy{font-family:var(--sans);font-size:10.5px;line-height:17px;color:var(--text);margin:10px auto 0;width:170px}
.card .btn{margin-top:12px;font-size:11px;letter-spacing:3px}

/* about */
.about-kicker{position:absolute;left:0;top:3192px;width:1200px;text-align:center;font-size:26px;letter-spacing:2px}
.about-title{position:absolute;left:0;top:3222px;width:1200px;text-align:center;font-size:62px;font-style:italic;letter-spacing:1px}
.video{position:absolute;left:236px;top:3320px;width:728px;height:242px;background:linear-gradient(90deg,#8d7a4e 0%,#c7b07a 45%,#9a8556 70%,#5e4a35 100%)}
.video-label{position:absolute;top:100px;font-size:34px;font-style:italic;letter-spacing:3px;color:rgba(255,255,255,.45)}
.play{position:absolute;left:344px;top:101px;width:40px;height:40px;border-radius:50%;background:var(--white)}
.about-copy{position:absolute;left:300px;top:3598px;width:600px;text-align:center;font-family:var(--sans);font-size:12px;line-height:22px;color:var(--text)}
.about-copy p+p{margin-top:18px}
.about-btn{position:absolute;left:513px;top:3790px}

/* footer */
.site-footer{position:absolute;left:0;top:3930px;width:1200px;height:325px;background:var(--footer);color:var(--white)}
.to-top{position:absolute;left:575px;top:-24px;width:50px;height:50px;border-radius:50%;background:var(--white);color:var(--ink);font-size:8px;letter-spacing:1px;text-align:center;padding-top:16px;line-height:10px}
.footer-nav{position:absolute;left:0;top:68px;width:1200px;display:flex;justify-content:center}
.footer-nav a{font-size:11px;letter-spacing:1.5px;color:var(--white);text-decoration:none;width:110px;text-align:center}
.copyright{position:absolute;left:0;top:105px;width:1200px;text-align:center;font-size:10px;letter-spacing:1.5px}
.social{position:absolute;left:514px;top:138px;display:flex;gap:10px}
.social span{width:24px;height:24px;border-radius:50%;background:#bdbdbd}
.footer-brand{position:absolute;left:0;top:205px;width:1200px;text-align:center;font-size:64px;color:var(--white);letter-spacing:1px}
</style>
</head>
<body>

<header class="site-header">
  <div class="brand">Tide Hollow 7</div>
  <nav class="main-nav">
    <a href="#">Home</a><a href="#">Shop</a><a href="#">About</a><a href="#">Charity</a><a href="#">Locations</a><a href="#">Contact</a>
  </nav>
  <svg class="cart" width="22" height="28" viewBox="0 0 22 28" aria-label="Shopping bag">
    <path d="M2 9h18l-1 18H3z" fill="none" stroke="#111" stroke-width="1.3"/>
    <path d="M7 9V6a4 4 0 0 1 8 0v3" fill="none" stroke="#111" stroke-width="1.3"/>
  </svg>
</header>

<section class="hero" role="img" aria-label="Portrait of a woman with long curly hair wearing a red and turquoise beaded necklace">
  <div class="hero-title hero-kicker">JEWELLERY</div>
  <div class="hero-title hero-main">ART AND FASHION</div>
  <div class="hero-title hero-sub">INDUSTRY</div>
  <div class="slider-dots"><span class="on"></span><span></span><span></span><span></span></div>
</section>

<section class="welcome">
  <div class="eyebrow">Welcome to</div>
  <h1 class="display" style="font-weight:400">Tide Hollow 7</h1>
  <p class="copy">Tide Hollow 7 curates chic jewellery, art and fashion pieces for people who value quiet luxury. Each item is chosen by hand for its craft, its materials and the story it carries into your home and wardrobe.</p>
  <p class="copy" style="margin-top:22px">New collections arrive each season, from beaded necklaces and leather wraps to home accents and modern womenswear.</p>
  <a class="btn" href="#">Continue reading »</a>
</section>
<div class="welcome-photo" role="img" aria-label="Turquoise and grey beaded necklaces with silver coin pendants on a wooden board"></div>

<div class="offer-bg">20% OFFER</div>
<div class="offer-kicker">EXCLUSIVE</div>
<h2 class="offer-title" style="font-weight:400">COLLECTIONS</h2>

<!-- row 1 -->
<div class="tile" style="left:100px;top:1550px;width:320px;height:506px">
  <div class="tile-photo" role="img" aria-label="Grey braided leather bracelets with a silver medallion" style="background:linear-gradient(160deg,#6f7480,#3e4450 60%,#8a8f98)"></div>
  <div class="card" style="left:58px;top:240px;width:206px;height:214px">
    <div class="card-tag">Fashion</div>
    <div class="card-title">2016</div>
    <div class="card-sub">Collections</div>
    <p class="card-copy">Hand-picked pieces finished with care and detail.</p>
    <a class="btn" href="#">Shop now »</a>
  </div>
</div>
<div class="tile" style="left:440px;top:1550px;width:660px;height:506px">
  <div class="tile-photo" role="img" aria-label="Turquoise and tan leather wrap bracelets with gold chain" style="background:linear-gradient(120deg,#d9c7b4,#3aa3b8 35%,#c8894d 75%,#e6d8c8)"></div>
  <div class="card" style="left:146px;top:270px;width:286px;height:192px">
    <div class="card-tag">Trendy Pearly</div>
    <div class="card-title italic" style="font-size:26px">Special <span class="card-sub small">collections</span></div>
    <p class="card-copy">Hand-picked pieces finished with care and detail.</p>
    <a class="btn" href="#">Shop now »</a>
  </div>
</div>

<!-- row 2 -->
<div class="tile" style="left:100px;top:2075px;width:320px;height:510px">
  <div class="tile-photo" role="img" aria-label="Fashion portrait of a woman seated in a white sweater" style="background:linear-gradient(170deg,#e6d4c2,#c9a47e 50%,#efe6dc)"></div>
  <div class="card" style="left:58px;top:240px;width:206px;height:214px">
    <div class="card-tag">Fashion</div>
    <div class="card-title">Girls</div>
    <div class="card-sub">Collections</div>
    <p class="card-copy">Hand-picked pieces finished with care and detail.</p>
    <a class="btn" href="#">Shop now »</a>
  </div>
</div>
<div class="tile" style="left:440px;top:2075px;width:320px;height:510px">
  <div class="tile-photo" role="img" aria-label="Silver coin pendants with turquoise beads" style="background:linear-gradient(150deg,#d8d3cc,#8f9aa0 45%,#6cb0b3 70%,#ddd6cf)"></div>
  <div class="card" style="left:58px;top:240px;width:206px;height:214px">
    <div class="card-tag">Fashion</div>
    <div class="card-title">Lean Line</div>
    <div class="card-sub">Collections</div>
    <p class="card-copy">Hand-picked pieces finished with care and detail.</p>
    <a class="btn" href="#">Shop now »</a>
  </div>
</div>
<div class="tile" style="left:780px;top:2075px;width:320px;height:510px">
  <div class="tile-photo" role="img" aria-label="Navy braided bracelets with gold chain" style="background:linear-gradient(140deg,#232a5c,#1a2050 50%,#3b3f6e)"></div>
  <div class="card" style="left:32px;top:140px;width:256px;height:230px">
    <div class="card-tag">Fashion</div>
    <div class="card-title">2016</div>
    <div class="card-sub">Collections</div>
    <p class="card-copy">Hand-picked pieces finished with care and detail.</p>
    <a class="btn" href="#">Shop now »</a>
  </div>
</div>

<!-- row 3 -->
<div class="tile" style="left:100px;top:2605px;width:320px;height:510px">
  <div class="tile-photo" role="img" aria-label="Grey leather braided bracelet with gold chain" style="background:linear-gradient(160deg,#9aa0a8,#5a6270 55%,#b9bdc2)"></div>
  <div class="card" style="left:58px;top:240px;width:206px;height:214px">
    <div class="card-tag">Fashion</div>
    <div class="card-title">Luxy</div>
    <div class="card-sub">Collections</div>
    <p class="card-copy">Hand-picked pieces finished with care and detail.</p>
    <a class="btn" href="#">Shop now »</a>
  </div>
</div>
<div class="tile" style="left:440px;top:2605px;width:660px;height:510px">
  <div class="tile-photo" role="img" aria-label="Metallic bronze leather cuff with a druzy stone" style="background:radial-gradient(circle at 45% 30%,#a07a62,#6c5244 45%,#cfc9c4 80%)"></div>
  <div class="card" style="left:146px;top:256px;width:286px;height:200px">
    <div class="card-tag">Trendy Pearly</div>
    <div class="card-title italic" style="font-size:26px">Gift <span class="card-sub small">collections</span></div>
    <p class="card-copy">Hand-picked pieces finished with care and detail.</p>
    <a class="btn" href="#">Shop now »</a>
  </div>
</div>

<!-- about -->
<div class="about-kicker">ABOUT</div>
<h2 class="about-title" style="font-weight:400">TIDE HOLLOW 7</h2>
<div class="video" role="img" aria-label="Fashion video still of a blonde woman">
  <span class="video-label" style="left:160px">FASHION</span>
  <span class="play"></span>
  <svg class="abs" style="left:359px;top:114px" width="12" height="14" viewBox="0 0 12 14"><path d="M1 1l10 6-10 6z" fill="#555"/></svg>
  <span class="video-label" style="left:404px">VIDEO</span>
</div>
<div class="about-copy">
  <p>Our studio began with a single bracelet and a love of fine materials. Today we work with small makers to bring together jewellery, art and fashion that feels personal, timeless and made to last for many seasons ahead.</p>
  <p>Every order is packed by hand and shipped with a note from our team, so each piece arrives ready to be worn.</p>
</div>
<a class="btn about-btn" href="#">Continue reading »</a>

<footer class="site-footer">
  <div class="to-top">▲<br>TOP</div>
  <nav class="footer-nav">
    <a href="#">HOME</a><a href="#">SHOP</a><a href="#">ABOUT</a><a href="#">CHARITY</a><a href="#">LOCATIONS</a><a href="#">CONTACT</a>
  </nav>
  <div class="copyright">COPYRIGHT © TIDE HOLLOW 7. ALL RIGHTS RESERVED.</div>
  <div class="social" aria-label="Social links"><span></span><span></span><span></span><span></span><span></span></div>
  <div class="footer-brand">Tide Hollow 7</div>
</footer>

</body>
</html>
```